Design business card for new business which advocates for elders in nursing homes or personal care h

New business for rights of the elderly residents who reside in personal care homes and or nursing homes. I am looking for a business card with logo of keystone for Pennsylvania and something in side the keystone that represents healthcare, advocates, something on that line; monitor care received and needs of resident. Chart audits, State Regulation compliance

Target Market(s)

Seniors no longer safe to live at home by themselves along with their kids

Industry/Entity Type

Business

Contact Information for Business Card

Keystone symbol to represent Pensylvaoa with some kind of symbol inside to represent advocate, seniors, or healthcare symbol

Font styles to use
Serif

Colors
33a6d7
85cae6
abd037

Requirements
Must have
• Brightwell Elder Allies is our business name; our tag line is Path to Better Living
Nice to have
• Nice logo

```html
<!DOCTYPE html>
<html lang="en">
<head>
<meta charset="utf-8">
<title>Brightwell Elder Allies — Business Card</title>
<link href="https://fonts.googleapis.com/css2?family=Open+Sans:wght@400;600;700;800&family=Comic+Neue:wght@700&display=swap" rel="stylesheet">
<style>
  :root {
    --brand-blue: #2ea3d5;
    --brand-light-blue: #85cae6;
    --brand-green: #a3c93a;
    --ink-dark: #3f3f3f;
    --ink-grey: #8a8a8a;
    --card-white: #f7f7f5;
    --panel-grey: #ebebea;
    --page-bg: #d9d9d9;
  }
  * { box-sizing: border-box; margin: 0; padding: 0; }
  html, body {
    width: 1200px; height: 750px; overflow: hidden;
    background: var(--page-bg);
    font-family: "Open Sans", Arial, sans-serif;
  }
  .canvas {
    width: 1200px; height: 750px;
    display: flex; flex-direction: column; align-items: center; justify-content: center;
    gap: 36px;
  }
  .card {
    width: 560px; height: 320px;
    position: relative; overflow: hidden;
    box-shadow: 0 6px 18px rgba(0,0,0,0.18);
  }

  /* Front */
  .card-front {
    background: var(--brand-blue);
    display: flex; flex-direction: column; align-items: center; justify-content: center;
    color: #fff;
  }
  .front-mark {
    width: 54px; height: 54px;
    background: #fff;
    margin-bottom: 18px;
  }
  .front-name {
    font-weight: 800; font-size: 34px; letter-spacing: 0.5px;
    text-transform: uppercase; text-align: center; line-height: 1.1;
  }

  /* Back */
  .card-back { background: var(--card-white); display: flex; }
  .back-brand {
    width: 52%;
    display: flex; flex-direction: column; align-items: center; justify-content: center;
    padding: 0 20px;
  }
  .brand-mark {
    width: 46px; height: 46px;
    background: var(--brand-blue);
    margin-bottom: 14px;
  }
  .brand-name {
    font-weight: 800; font-size: 24px; color: var(--ink-dark);
    text-transform: uppercase; text-align: center; line-height: 1.15;
  }
  .brand-tagline {
    margin-top: 14px;
    font-family: "Comic Neue", "Comic Sans MS", cursive;
    font-weight: 700; font-size: 19px; color: var(--brand-green);
  }
  .back-contact {
    width: 48%;
    background: var(--panel-grey);
    position: relative;
    padding-top: 98px;
  }
  .name-band {
    background: var(--brand-green);
    margin-left: -12px;
    padding: 6px 18px 6px 28px;
    color: #fff;
  }
  .person-name { font-weight: 700; font-size: 17px; letter-spacing: 0.3px; line-height: 1.15; }
  .person-role { font-size: 12px; color: #eef5d8; line-height: 1.2; }
  .contact-block {
    position: relative;
    margin-top: 14px;
    padding-left: 28px;
    font-size: 13.5px; color: #222; line-height: 1.35;
  }
  .contact-block::before {
    content: ""; position: absolute; left: 0; top: -8px;
    width: 9px; height: 62px; background: var(--brand-green);
  }
  .contact-address { margin-bottom: 10px; }
  .contact-line { margin-bottom: 6px; }
</style>
</head>
<body>
<main class="canvas">
  <section class="card card-front" aria-label="Card front">
    <div class="front-mark" aria-hidden="true"></div>
    <p class="front-name">Brightwell<br>Elder Allies</p>
  </section>

  <section class="card card-back" aria-label="Card back">
    <div class="back-brand">
      <div class="brand-mark" aria-hidden="true"></div>
      <p class="brand-name">Brightwell<br>Elder Allies</p>
      <p class="brand-tagline">Path to Better Living</p>
    </div>
    <div class="back-contact">
      <div class="name-band">
        <p class="person-name">PERSON NAME</p>
        <p class="person-role">CEO/Owner</p>
      </div>
      <div class="contact-block">
        <p class="contact-address">your street address<br>goes here</p>
        <p class="contact-line">p : +100 5550 2714</p>
        <p class="contact-line">e : yourid@brightwell.com</p>
      </div>
    </div>
  </section>
</main>
</body>
</html>
```